Innovative coffee bean bag design for roasters

We need a design which can be printed on a coffee bean bag but which could also work on a sticker of similar size. We're after quirky, geeky, playful and innovative. Something that will stand out and communicate the character of our business. It should be eye catching and draw the customer in for a closer look.
Thematically, think organic and earthy.
It needs an element which can be changed for different coffee origins and roast profiles, so the main design will remain the same but with a feature which changes to help the customer know what they're looking at and will make them smile.
Approximate dimensions we need are 15cm by 12cm, with the 15cm being the vertical height of the bag image. (The image will be viewed in portrait). This is the main print area - however, if you have a great idea for a full bag image (approximately 23cm by 13cm), feel free to submit this too, we're interested in all ideas.
There is an image attached of a white partially see-through bag which we are considering using, so keep this in mind when designing.
We will need our logo including - see attached image.
Finally, we need space for the information about the coffee, such as origin, roast profile, flavour notes - see attached image for an example of the information (not necessarily a stylistic indicator). Please suggest fonts etc.

Target Market(s)

coffee roasters

Requirements
Must have
• Must say under the logo coffee roasters( Quiet Fennel Organic Coffee Roasters )
Nice to have
• Unique symbol, shapes, scientific.

```html
<!DOCTYPE html>
<html lang="en">
<head>
<meta charset="utf-8">
<title>Quiet Fennel Organic Coffee Roasters – Label Range</title>
<link rel="stylesheet" href="https://fonts.googleapis.com/css2?family=Abril+Fatface&family=Oswald:wght@500;600&family=Archivo:wght@500;700&display=swap">
<style>
  :root {
    --orange: #f6813a;
    --green: #7cc24f;
    --teal: #4fe3c3;
    --purple: #a57cc9;
    --accent-orange: #f47a34;
    --accent-purple: #9b6fc8;
    --accent-teal: #4fe3c3;
    --cream: #f5ead9;
    --ink: #1d1d1d;
    --paper: #ffffff;
    --brand-brown: #6b3a1f;
  }
  * { box-sizing: border-box; margin: 0; padding: 0; }
  html, body { width: 1200px; height: 800px; overflow: hidden; background: var(--paper); }
  .range {
    display: flex; gap: 50px; justify-content: center; align-items: center;
    width: 1200px; height: 800px;
  }
  .label {
    position: relative; width: 240px; height: 300px;
    border-radius: 14px; overflow: hidden; background: var(--bg);
  }
  .label--orange { --bg: var(--orange); }
  .label--green  { --bg: var(--green); }
  .label--teal   { --bg: var(--teal); }
  .label--purple { --bg: var(--purple); }

  .brand-head { position: absolute; inset: 0 0 auto 0; height: 150px; }
  .maker-badge {
    position: absolute; top: 17px; left: 50%; transform: translateX(-50%);
    display: flex; align-items: center; gap: 5px; white-space: nowrap;
    background: var(--paper); border-radius: 14px; padding: 4px 11px;
  }
  .maker-badge__dot { width: 9px; height: 9px; border-radius: 50%; background: var(--brand-brown); }
  .maker-badge__name {
    font-family: "Archivo", sans-serif; font-weight: 700; font-size: 9px;
    letter-spacing: 0.5px; color: var(--brand-brown); text-transform: uppercase;
  }
  .wordmark { position: absolute; left: 27px; top: 64px; color: var(--paper); font-weight: 400; }
  .wordmark__small {
    display: block; font-family: "Abril Fatface", serif; font-size: 17px;
    line-height: 1; margin-left: 24px;
  }
  .wordmark__big {
    display: block; font-family: "Abril Fatface", serif; font-size: 40px;
    line-height: 0.9; letter-spacing: 0.5px;
  }
  .wordmark__tag {
    position: absolute; left: 28px; top: 121px; white-space: nowrap;
    font-family: "Oswald", sans-serif; font-weight: 500; font-size: 10.5px;
    letter-spacing: 1.3px; color: var(--paper); text-transform: uppercase;
  }
  .cup-mark {
    position: absolute; right: 26px; top: 74px; width: 32px; height: 56px;
    border-radius: 16px 16px 10px 10px; background: rgba(255,255,255,0.25);
  }

  .origin-strip {
    position: absolute; left: 0; top: 150px; width: 50px; height: 150px;
    background: linear-gradient(180deg, var(--accent-teal) 0%, var(--accent-orange) 45%, var(--accent-purple) 100%);
  }
  .info-panel {
    position: absolute; left: 50px; top: 150px; width: 190px; height: 114px;
    background: var(--paper); display: flex;
  }
  .origin-name {
    width: 26px; display: flex; align-items: center; justify-content: center;
    border-right: 1.5px solid var(--ink); margin: 10px 0;
  }
  .origin-name span {
    transform: rotate(-90deg); white-space: nowrap;
    font-family: "Oswald", sans-serif; font-weight: 600; font-size: 17px;
    letter-spacing: 2px; color: var(--ink);
  }
  .coffee-facts { flex: 1; padding: 8px 12px 4px 12px; display: flex; flex-direction: column; }
  .facts-row {
    flex: 1; display: grid; grid-template-columns: 1fr 1fr; align-items: start;
    padding-top: 4px;
  }
  .facts-row + .facts-row { border-top: 1px solid var(--ink); }
  .fact {
    font-family: "Archivo", sans-serif; font-size: 6px; line-height: 1.05;
    color: var(--ink); text-transform: uppercase; font-weight: 500; white-space: nowrap;
  }
  .fact b { display: block; font-weight: 700; }
  .pattern-band {
    position: absolute; left: 50px; top: 264px; width: 190px; height: 36px;
    background: linear-gradient(90deg, var(--accent-teal) 0%, var(--accent-orange) 35%, var(--accent-purple) 70%, var(--cream) 100%);
  }
</style>
</head>
<body>
<main class="range">

  <article class="label label--orange">
    <header class="brand-head">
      <div class="maker-badge"><span class="maker-badge__dot"></span><span class="maker-badge__name">Copper Kettle</span></div>
      <h1 class="wordmark"><span class="wordmark__small">Quiet</span><span class="wordmark__big">Fennel</span></h1>
      <p class="wordmark__tag">Organic Coffee Roasters</p>
      <div class="cup-mark" role="img" aria-label="Steaming coffee cup illustration"></div>
    </header>
    <div class="origin-strip" role="img" aria-label="Geometric tile column with bean, leaf and arc motifs"></div>
    <section class="info-panel">
      <div class="origin-name"><span>COLOMBIA</span></div>
      <div class="coffee-facts">
        <div class="facts-row"><p class="fact">Process:<b>Washed</b></p><p class="fact">Varieties:<b>Caturra</b></p></div>
        <div class="facts-row"><p class="fact">Farm:<b>La Colina</b></p><p class="fact">Producer:<b>Mateo Ruiz</b></p></div>
        <div class="facts-row"><p class="fact">Location:<b>Huila</b></p><p class="fact">Roast<br>Date:</p></div>
      </div>
    </section>
    <div class="pattern-band" role="img" aria-label="Geometric tile band with dots and arcs"></div>
  </article>

  <article class="label label--green">
    <header class="brand-head">
      <div class="maker-badge"><span class="maker-badge__dot"></span><span class="maker-badge__name">Copper Kettle</span></div>
      <h1 class="wordmark"><span class="wordmark__small">Quiet</span><span class="wordmark__big">Fennel</span></h1>
      <p class="wordmark__tag">Organic Coffee Roasters</p>
      <div class="cup-mark" role="img" aria-label="Steaming coffee cup illustration"></div>
    </header>
    <div class="origin-strip" role="img" aria-label="Geometric tile column with bean, leaf and arc motifs"></div>
    <section class="info-panel">
      <div class="origin-name"><span>COLOMBIA</span></div>
      <div class="coffee-facts">
        <div class="facts-row"><p class="fact">Process:<b>Washed</b></p><p class="fact">Varieties:<b>Caturra</b></p></div>
        <div class="facts-row"><p class="fact">Farm:<b>La Colina</b></p><p class="fact">Producer:<b>Mateo Ruiz</b></p></div>
        <div class="facts-row"><p class="fact">Location:<b>Huila</b></p><p class="fact">Roast<br>Date:</p></div>
      </div>
    </section>
    <div class="pattern-band" role="img" aria-label="Geometric tile band with dots and arcs"></div>
  </article>

  <article class="label label--teal">
    <header class="brand-head">
      <div class="maker-badge"><span class="maker-badge__dot"></span><span class="maker-badge__name">Copper Kettle</span></div>
      <h1 class="wordmark"><span class="wordmark__small">Quiet</span><span class="wordmark__big">Fennel</span></h1>
      <p class="wordmark__tag">Organic Coffee Roasters</p>
      <div class="cup-mark" role="img" aria-label="Steaming coffee cup illustration"></div>
    </header>
    <div class="origin-strip" role="img" aria-label="Geometric tile column with bean, leaf and arc motifs"></div>
    <section class="info-panel">
      <div class="origin-name"><span>COLOMBIA</span></div>
      <div class="coffee-facts">
        <div class="facts-row"><p class="fact">Process:<b>Washed</b></p><p class="fact">Varieties:<b>Caturra</b></p></div>
        <div class="facts-row"><p class="fact">Farm:<b>La Colina</b></p><p class="fact">Producer:<b>Mateo Ruiz</b></p></div>
        <div class="facts-row"><p class="fact">Location:<b>Huila</b></p><p class="fact">Roast<br>Date:</p></div>
      </div>
    </section>
    <div class="pattern-band" role="img" aria-label="Geometric tile band with dots and arcs"></div>
  </article>

  <article class="label label--purple">
    <header class="brand-head">
      <div class="maker-badge"><span class="maker-badge__dot"></span><span class="maker-badge__name">Copper Kettle</span></div>
      <h1 class="wordmark"><span class="wordmark__small">Quiet</span><span class="wordmark__big">Fennel</span></h1>
      <p class="wordmark__tag">Organic Coffee Roasters</p>
      <div class="cup-mark" role="img" aria-label="Steaming coffee cup illustration"></div>
    </header>
    <div class="origin-strip" role="img" aria-label="Geometric tile column with bean, leaf and arc motifs"></div>
    <section class="info-panel">
      <div class="origin-name"><span>COLOMBIA</span></div>
      <div class="coffee-facts">
        <div class="facts-row"><p class="fact">Process:<b>Washed</b></p><p class="fact">Varieties:<b>Caturra</b></p></div>
        <div class="facts-row"><p class="fact">Farm:<b>La Colina</b></p><p class="fact">Producer:<b>Mateo Ruiz</b></p></div>
        <div class="facts-row"><p class="fact">Location:<b>Huila</b></p><p class="fact">Roast<br>Date:</p></div>
      </div>
    </section>
    <div class="pattern-band" role="img" aria-label="Geometric tile band with dots and arcs"></div>
  </article>

</main>
</body>
</html>
```